Quietude Lantern Habits book cover

Hello!
I need a 5.25x8 VNR paperback cover and ZOB audiobook square cover with the same design. (I might need a Spanish copy as well, but that should just be copy and pasting the translation after the winner is chosen, so don't worry about that for now.)
The title text should be laid out something like this:
A QUICK
WHAT, WHO, WHY, WHERE, HOW & WHEN
-----OF-----
QUIETUDE
LANTERN HABITS
The book should be about 160 pages, for the spine width.
I have attached some concepts/ideas I have for inspiration, but feel free to submit any kinds of ideas you might have. I'm open to your creativity!
~~~~~~~~
Back Sleeve Summary:
Countless studies and anecdotal reports have shown that large doses of psilocybin mushrooms can inspire breakthroughs and mystical experiences or help relieve symptoms of mental health disorders and physical ailments. However, macrodosing psychedelics doesn’t always have a practical application in our day-to-day lives.
Enter microdosing: a method of taking small amounts of psychedelics to invoke a desirable physiological response with minimal undesirable drawbacks. The practice has become more popular in recent years and is proving to be a safe and powerful approach not only to addressing an array of health concerns but also to improving general performance.
Whether you’re looking to taper off pharmaceuticals or simply improve your mood, creativity, sleep, eating habits, physical stamina, or sexual performance, this book will help you learn how microdosing could improve your overall quality of life. The information herein also doesn’t shy away from addressing more controversial topics, such as microdosing in youth or during pregnancy.
This book is intended to provide foundational knowledge of what microdosing is, who is doing it, various motivations for doing so, ideal times and protocols for practice, considerations for where to microdose, and how to go about sourcing and dosing psilocybin mushrooms. It is a carefully researched, beginner-friendly guide that weaves together concise history and research with practical application and integration of microdosing psilocybin.
Author Section (with attached photo):
Dale Pemberton earned a B.S. in Kinesiology from the University of Harwick Vale, and has furthered his studies in the fields of psychedelics, psychology, and trauma healing since 2012. He’s been exploring the benefits of psychedelics within himself for equally as long.
People interested in self help, healing, and microdosing psychedelics.

```html
<!DOCTYPE html>
<html lang="es">
<head>
<meta charset="utf-8">
<title>Quietude Lantern Habits — cubierta</title>
<link href="https://fonts.googleapis.com/css2?family=Bebas+Neue&family=Oswald:wght@500&family=Montserrat:wght@300;400&display=swap" rel="stylesheet">
<style>
  :root {
    --paper: #fafafa;
    --ink: #3a3a3a;
    --body-ink: #3d3d3d;
    --accent: #00aeef;
    --frame: #b9b9b9;
    --art-top: #0d4a86;
    --art-mid: #070a12;
    --art-low: #7a5622;
  }
  * { margin: 0; padding: 0; box-sizing: border-box; }
  html, body { width: 1200px; height: 873px; overflow: hidden; background: var(--paper); }
  .cover { position: relative; width: 1200px; height: 873px; background: var(--paper); }
  svg text { font-family: "Bebas Neue", "Oswald", sans-serif; }
  .title-block { position: absolute; display: block; overflow: visible; }
  .t-ink { fill: var(--ink); }
  .t-accent { fill: var(--accent); }
  .rule { stroke: var(--accent); }

  .back-blurb {
    position: absolute; left: 44px; top: 198px; width: 485px;
    font-family: "Montserrat", sans-serif; font-weight: 300;
    font-size: 12.6px; line-height: 15.5px; color: var(--body-ink);
    text-align: justify;
  }
  .back-blurb p + p { margin-top: 6px; }

  .author-rule { position: absolute; left: 42px; width: 489px; height: 1px; background: var(--accent); }
  .author-photo {
    position: absolute; left: 44px; top: 545px; width: 190px; height: 110px;
    background: linear-gradient(135deg, #3b3b3b 0%, #8a8a8a 45%, #d8d8d8 70%, #6b6b6b 100%);
  }
  .author-bio {
    position: absolute; left: 246px; top: 544px; width: 283px;
    font-family: "Montserrat", sans-serif; font-weight: 300;
    font-size: 12.4px; line-height: 15.5px; color: var(--body-ink);
    text-align: justify;
  }
  .barcode-space {
    position: absolute; left: 359px; top: 701px; width: 173px; height: 114px;
    background: #fff; border: 1px solid var(--frame);
  }

  .spine { position: absolute; left: 572px; top: 0; width: 56px; height: 873px; }

  .cover-art {
    position: absolute; left: 730px; top: 315px; width: 350px; height: 400px;
    background: linear-gradient(180deg, var(--art-top) 0%, var(--art-mid) 50%, var(--art-low) 100%);
  }
</style>
</head>
<body>
<main class="cover">

  <!-- Back cover -->
  <svg class="title-block" style="left:140px;top:58px" width="300" height="128" viewBox="0 0 300 128" aria-label="Un breve resumen de qué, quién, por qué, dónde, cómo y cuándo consumir de Quietude Lantern Habits">
    <text class="t-ink" x="150" y="20" font-size="21" text-anchor="middle">UN BREVE</text>
    <text class="t-ink" x="19" y="32" font-size="10.5" textLength="262" lengthAdjust="spacingAndGlyphs">RESUMEN DE QUÉ, QUIÉN, POR QUÉ, DÓNDE, CÓMO Y CUÁNDO CONSUMIR</text>
    <line class="rule" x1="19" y1="42" x2="135" y2="42" stroke-width="1.2"/>
    <line class="rule" x1="165" y1="42" x2="281" y2="42" stroke-width="1.2"/>
    <text class="t-ink" x="150" y="47" font-size="15" text-anchor="middle">DE</text>
    <text class="t-accent" x="19" y="96" font-size="58" textLength="262" lengthAdjust="spacingAndGlyphs">QUIETUDE</text>
    <text class="t-accent" x="19" y="126" font-size="32" textLength="262" lengthAdjust="spacingAndGlyphs">LANTERN HABITS</text>
  </svg>

  <div class="back-blurb">
    <p>Innumerables estudios e informes han demostrado que grandes dosis de hongos psilocibios pueden ayudar a aliviar los síntomas de trastornos mentales o dolencias físicas. Sin embargo, la macrodosificación de psicodélicos no siempre tiene una aplicación práctica en nuestra vida diaria.</p>
    <p>La microdosificación es un método que consiste en tomar pequeñas cantidades de psicodélicos para inducir una respuesta fisiológica deseable con mínimas consecuencias negativas. Esta práctica está ganando popularidad y demuestra ser un enfoque seguro y eficaz para abordar problemas de salud y mejorar el rendimiento. Ya sea que busque reducir gradualmente la dosis de fármacos o simplemente mejorar su estado de ánimo, creatividad, sueño, hábitos alimenticios, resistencia física o rendimiento sexual, este libro le ayudará a aprender cómo la microdosificación podría mejorar su calidad de vida en general.</p>
    <p>Este libro pretende proporcionar conocimientos básicos sobre qué es la microdosificación, quién la practica, las diversas motivaciones para hacerlo, los momentos y protocolos ideales para la práctica, consideraciones sobre dónde microdosificar y cómo obtener y dosificar hongos psilocibios. Es una guía para principiantes, cuidadosamente investigada, que combina una historia concisa y una investigación con la aplicación práctica y la integración de la microdosificación de psilocibina.</p>
  </div>

  <div class="author-rule" style="top:536px"></div>
  <div class="author-photo" role="img" aria-label="Retrato en blanco y negro del autor sentado en una oficina"></div>
  <p class="author-bio">Dale Pemberton se licenció en Kinesiología en la Universidad de Harwick Vale y ha ampliado sus estudios en los campos de los psicodélicos, la psicología y la sanación de traumas desde 2012. Desde entonces, ha explorado los beneficios de los psicodélicos en su propia experiencia.</p>
  <div class="author-rule" style="top:667px"></div>
  <div class="barcode-space"></div>

  <!-- Spine -->
  <svg class="spine" width="56" height="873" viewBox="0 0 56 873" aria-label="Lomo: Quietude Lantern Habits, Dale Pemberton">
    <text class="t-accent" transform="translate(13 82) rotate(90)" font-size="27" textLength="426" lengthAdjust="spacing">QUIETUDE LANTERN HABITS</text>
    <text class="t-ink" transform="translate(38 80) rotate(90)" font-size="11.5" textLength="425" lengthAdjust="spacingAndGlyphs">UN BREVE RESUMEN DE QUÉ, QUIÉN, POR QUÉ, DÓNDE, CÓMO Y CUÁNDO CONSUMIR DE</text>
    <text class="t-ink" transform="translate(22 577) rotate(90)" font-size="22" textLength="217" lengthAdjust="spacing">DALE PEMBERTON</text>
  </svg>

  <!-- Front cover -->
  <svg class="title-block" style="left:680px;top:56px" width="468" height="230" viewBox="0 0 468 230" aria-label="Un breve resumen de qué, quién, por qué, dónde, cómo y cuándo consumir de Quietude Lantern Habits">
    <text class="t-ink" x="234" y="34" font-size="39" text-anchor="middle">UN BREVE</text>
    <text class="t-ink" x="5" y="57" font-size="20" textLength="457" lengthAdjust="spacingAndGlyphs">RESUMEN DE QUÉ, QUIÉN, POR QUÉ, DÓNDE, CÓMO Y CUÁNDO CONSUMIR</text>
    <line class="rule" x1="5" y1="74" x2="213" y2="74" stroke-width="2"/>
    <line class="rule" x1="256" y1="74" x2="462" y2="74" stroke-width="2"/>
    <text class="t-ink" x="234" y="83" font-size="27" text-anchor="middle">DE</text>
    <text class="t-accent" x="5" y="166" font-size="104" textLength="457" lengthAdjust="spacingAndGlyphs">QUIETUDE</text>
    <text class="t-accent" x="5" y="222" font-size="54" textLength="457" lengthAdjust="spacingAndGlyphs">LANTERN HABITS</text>
  </svg>

  <div class="cover-art" role="img" aria-label="Ilustración de cubierta: cabeza en papel rasgado con un cerebro azul luminoso y hongos dorados"></div>

  <svg class="title-block" style="left:752px;top:782px" width="325" height="42" viewBox="0 0 325 42" aria-label="Dale Pemberton">
    <text class="t-ink" x="5" y="36" font-size="40" textLength="314" lengthAdjust="spacing">DALE PEMBERTON</text>
  </svg>

</main>
</body>
</html>
```